Tolvern Business Cards

Business card design. dont mind if new logo is suggested.
it would be for a security company.
our clients would be bigger security companies around Australia.
have a logo done but can be replaced. see attaached. like the colors.
Need company name, person name, designation, phone and email on front.
At back company logo and name. website saddress and 2 x license numbers
would like to have 2 different background color for both sidde

Industry/Entity Type

Security

Contact Information for Business Card

round corners, front should be light in color. need logo at back with webaddress and 2 x license numners

Font styles to use
Sans Serif

Colors
f37122
faa54b
f8ba93
0255a3
0592cd
85cae6
b3d448
9bcb3c
ffffff

Requirements
Must have
• see description
Nice to have
• see description
Should not have
• should not be difficult to read or hardd to find information on card.. lets say easy on eyes yet catchy

```html
<!DOCTYPE html>
<html lang="en">
<head>
<meta charset="utf-8">
<title>Tolvern Security Group – Business Cards</title>
<link href="https://fonts.googleapis.com/css2?family=Cinzel:wght@600&family=Montserrat:wght@400;600&display=swap" rel="stylesheet">
<style>
  :root {
    --stage: #2e2e2e;
    --navy: #1e3160;
    --navy-text: #1b2b5e;
    --cyan: #0592cd;
    --light-cyan: #85cae6;
    --white: #ffffff;
    --grey-text: #7a7a7a;
    --contact-text: #6b6b6b;
  }
  * { margin: 0; padding: 0; box-sizing: border-box; }
  html, body { width: 1200px; height: 864px; overflow: hidden; }
  body {
    background: var(--stage);
    font-family: "Montserrat", sans-serif;
    position: relative;
  }
  .card {
    position: absolute;
    left: 330px;
    width: 540px;
    height: 309px;
    border-radius: 22px;
  }
  .card-back {
    top: 103px;
    background: var(--navy);
    color: var(--white);
    display: flex;
    flex-direction: column;
    align-items: center;
    justify-content: center;
    text-align: center;
  }
  .brand-dot {
    width: 78px;
    height: 78px;
    border-radius: 50%;
    background: var(--cyan);
    margin-bottom: 22px;
  }
  .company-name {
    font-family: "Cinzel", serif;
    font-weight: 600;
    font-size: 25px;
    letter-spacing: 0.5px;
    margin-bottom: 14px;
  }
  .licenses, .back-website {
    font-size: 12.5px;
    letter-spacing: 0.6px;
    line-height: 1.5;
  }
  .card-front {
    top: 452px;
    background: var(--white);
  }
  .front-company {
    position: absolute;
    left: 0;
    right: 0;
    top: 40px;
    text-align: center;
    font-family: "Cinzel", serif;
    font-weight: 600;
    font-size: 14px;
    letter-spacing: 1px;
    color: var(--navy-text);
  }
  .front-content {
    position: absolute;
    left: 78px;
    top: 100px;
    display: flex;
    align-items: center;
  }
  .identity { text-align: right; padding-right: 18px; }
  .person-name {
    color: var(--navy-text);
    font-weight: 600;
    font-size: 26px;
    line-height: 1.1;
  }
  .designation {
    color: var(--grey-text);
    font-size: 14px;
    letter-spacing: 0.5px;
    margin-top: 2px;
  }
  .divider {
    width: 1.5px;
    height: 62px;
    background: var(--navy-text);
  }
  .contacts {
    list-style: none;
    padding-left: 16px;
    font-size: 13px;
    color: var(--contact-text);
    letter-spacing: 0.3px;
  }
  .contacts li { display: flex; align-items: center; line-height: 1.6; white-space: nowrap; }
  .contacts svg { width: 13px; height: 13px; margin-right: 8px; flex-shrink: 0; }
</style>
</head>
<body>
  <section class="card card-back" aria-label="Card back">
    <div class="brand-dot"></div>
    <h1 class="company-name">TOLVERN SECURITY GROUP</h1>
    <p class="licenses">License #0417382 &nbsp;-&nbsp; License #0417395</p>
    <p class="back-website">www.tolvernsecurity.com</p>
  </section>

  <section class="card card-front" aria-label="Card front">
    <p class="front-company">TOLVERN SECURITY GROUP</p>
    <div class="front-content">
      <div class="identity">
        <h2 class="person-name">Daniel Harrow</h2>
        <p class="designation">President</p>
      </div>
      <div class="divider"></div>
      <ul class="contacts">
        <li>
          <svg viewBox="0 0 16 16"><path d="M4 1.5 6.5 4 5 6c1 2 3 4 5 5l2-1.5 2.5 2.5-2 2.5C7 14 2 9 1.5 3.5Z" fill="var(--cyan)"/></svg>
          021-555-0148
        </li>
        <li>
          <svg viewBox="0 0 16 16"><rect x="1" y="3" width="14" height="10" fill="var(--cyan)"/><path d="M1 3 8 9 15 3" fill="none" stroke="var(--white)" stroke-width="1.3"/></svg>
          info@tolvernsecurity.com
        </li>
        <li>
          <svg viewBox="0 0 16 16" fill="none" stroke="var(--cyan)" stroke-width="1.3"><circle cx="8" cy="8" r="6.5"/><ellipse cx="8" cy="8" rx="3" ry="6.5"/><path d="M1.5 8h13M2.5 4.8h11M2.5 11.2h11"/></svg>
          www.tolvernsecurity.com
        </li>
      </ul>
    </div>
  </section>
</body>
</html>
```